Mental Health Counselor needs advertisement design for Men's and Woman's chorus programs

I need a 1/6th page advertisement for my mental health practice named 'Quillfern Mental Health' I primarily serve the LGBTQ community, providing individual and couples/family therapy. The ad should include a 'call to action' such as Call me I can help, or Schedule an appointment today. The final design should convey familiarity with the needs of the queer community and my unique ability to help the reader with emotional concerns or relationship issues.

I would like to see designs using my logo (attached 2015-Logo.eps) and the colors of my website http://www.quillfernmentalhealth.example particularly the banner imagery (attached indigo banner.jpg and indigoMH2015.ase, bannersource.jpg)

The ad must contain the following:
Quillfern Mental Health or Quillfern Mental Health Counseling
the website address www.quillfernmentalhealth.example
phone number 206-555-0147
and my name/title: Dorian K. Whitlow Jr. MA, LMHCA/LMFTA

I am attaching the guidelines for the ad and a pdf sample of their program,

Target Market(s)

Gay, Bisexual and Transgender clients with reasonable affluence, in their late 30's- late 50's

Industry/Entity Type

Mental Health

Font styles to use
Sans Serif
Other font styles liked:
• Clerica Medium, Open Sans Family

Colors
b7a5cd
d7cce4
0455a3
ffffff

Requirements
Must have
• Must use my Logo (2015-Logo.eps attached)
Should not have
• Biased or negative language.

```html
<!DOCTYPE html>
<html lang="en">
<head>
<meta charset="utf-8">
<title>Quillfern Mental Health – Program Ads</title>
<link rel="stylesheet" href="https://fonts.googleapis.com/css2?family=Open+Sans:ital,wght@0,400;0,600;0,700;1,700&family=Roboto+Condensed:wght@400;700&display=swap">
<style>
  :root {
    --indigo-deep: #231c5c;
    --indigo: #3a3080;
    --indigo-mid: #4a3f93;
    --lavender: #b7a5cd;
    --lavender-light: #d7cce4;
    --blue: #0455a3;
    --white: #ffffff;
    --accent-yellow: #f2e84a;
    --band-grey: #cfcbe0;
  }
  * { margin: 0; padding: 0; box-sizing: border-box; }
  html, body { width: 1200px; height: 1200px; overflow: hidden; background: var(--white); }
  .canvas { position: relative; width: 1200px; height: 1200px; }

  .ad { position: absolute; top: 467px; width: 410px; height: 205px; overflow: hidden; }
  .ad--classic { left: 196px; background: linear-gradient(180deg, var(--indigo-deep) 0%, var(--indigo) 45%, var(--indigo-mid) 100%); font-family: "Open Sans", sans-serif; color: var(--white); }
  .ad--modern { left: 640px; background: var(--indigo); font-family: "Roboto Condensed", sans-serif; color: var(--white); }

  .abs { position: absolute; white-space: nowrap; z-index: 2; }

  .brand { display: flex; align-items: center; gap: 10px; color: var(--lavender); font-weight: 400; }
  .brand__dot { border-radius: 50%; background: var(--lavender); flex: none; }
  .ad--classic .brand { left: 54px; top: 30px; font-size: 22px; }
  .ad--classic .brand__dot { width: 30px; height: 30px; }
  .ad--modern .brand { left: 8px; top: 22px; font-size: 14px; gap: 8px; font-family: "Open Sans", sans-serif; }
  .ad--modern .brand__dot { width: 26px; height: 26px; }

  .skyline { position: absolute; }
  .ad--classic .skyline { left: 0; top: 85px; width: 176px; height: 97px; background: linear-gradient(180deg, rgba(58,48,128,0) 0%, #2a2468 40%, #1a1545 100%); }
  .ad--classic .text-shade { position: absolute; left: 176px; top: 106px; width: 234px; height: 76px; background: linear-gradient(180deg, #2a2468 0%, #171338 100%); }
  .ad--modern .skyline { left: 0; top: 109px; width: 254px; height: 96px; background: linear-gradient(180deg, var(--indigo) 0%, #2b2660 35%, #3c2f3a 70%, #15152e 100%); }

  .service-band { left: 180px; top: 88px; width: 230px; height: 18px; background: var(--band-grey); clip-path: polygon(8px 0, 100% 0, 100% 100%, 0 100%); color: var(--indigo-deep); font-style: italic; font-weight: 700; font-size: 14px; letter-spacing: 4px; line-height: 18px; padding-left: 24px; }
  .ad--classic .cta { left: 196px; top: 110px; font-size: 12px; font-weight: 600; }
  .ad--classic .counselor { left: 196px; top: 127px; font-size: 14px; font-weight: 600; }
  .ad--classic .counselor small { font-size: 10px; font-weight: 700; }
  .ad--classic .phone { left: 196px; top: 144px; font-size: 18px; font-weight: 700; }
  .ad--classic .email { left: 196px; top: 168px; font-size: 8.5px; font-weight: 700; letter-spacing: 0.3px; }
  .footer-band { left: 0; top: 182px; width: 410px; height: 23px; background: var(--indigo-deep); text-align: center; font-size: 11px; font-weight: 700; letter-spacing: 1.6px; line-height: 23px; }

  .contact-panel { position: absolute; left: 0; top: 0; z-index: 1; }
  .ad--modern .r { right: 8px; text-align: right; }
  .ad--modern .service { top: 22px; font-size: 27px; font-weight: 700; letter-spacing: 3px; }
  .ad--modern .cta { top: 55px; font-size: 12.5px; font-weight: 700; }
  .ad--modern .counselor { top: 109px; font-size: 15px; font-weight: 700; }
  .ad--modern .credentials { top: 129px; font-size: 9px; font-weight: 700; }
  .ad--modern .phone { top: 140px; font-size: 28px; font-weight: 700; }
  .ad--modern .email, .ad--modern .web { font-family: "Open Sans", sans-serif; font-size: 8.5px; color: var(--accent-yellow); }
  .ad--modern .email { top: 173px; }
  .ad--modern .web { top: 187px; }
</style>
</head>
<body>
<div class="canvas">

  <section class="ad ad--classic" aria-label="Quillfern Mental Health advertisement, classic layout">
    <div class="abs brand"><span class="brand__dot"></span>Quillfern Mental Health</div>
    <div class="skyline" role="img" aria-label="Night city skyline photograph in indigo tones"></div>
    <div class="text-shade"></div>
    <div class="abs service-band">COUNSELING</div>
    <div class="abs cta">Schedule an Appointment Today</div>
    <div class="abs counselor">K. Whitlow Jr. MA <small>(LMHCA/LMFTA)</small></div>
    <div class="abs phone">(206) 555 0147</div>
    <div class="abs email">dorian@quillfernmentalhealth.example</div>
    <div class="abs footer-band">www.quillfernmentalhealth.example</div>
  </section>

  <section class="ad ad--modern" aria-label="Quillfern Mental Health advertisement, modern layout">
    <div class="abs brand"><span class="brand__dot"></span>Quillfern Mental Health</div>
    <div class="skyline" role="img" aria-label="City skyline at dusk with lit towers"></div>
    <svg class="contact-panel" width="410" height="205" viewBox="0 0 410 205" aria-hidden="true">
      <polygon points="254,0 197,97 250,205 410,205 410,0" fill="var(--blue)"/>
    </svg>
    <div class="abs r service">Counseling</div>
    <div class="abs r cta">Schedule an Appointment Today</div>
    <div class="abs r counselor">Dorian K. Whitlow Jr. MA</div>
    <div class="abs r credentials">(LMHCA/LMFTA)</div>
    <div class="abs r phone">206-555-0147</div>
    <div class="abs r email">dorian@quillfernmentalhealth.example</div>
    <div class="abs r web">www.quillfernmentalhealth.example</div>
  </section>

</div>
</body>
</html>
```